Business Card Design

We need a business card design for a consulting firm which provides safety and risk management consulting services for public venues, hotels and tourist attractions. The business card design should include the attached logo unedited with a design based on incorporating the existing logo with a design of geometric patterns or lines on a predominantly white background.

Industry/Entity Type

Business

Contact Information for Business Card

Dane Morvello
Director & Principal Consultant

Ph: +61 (0) 468502 174
PO Box 456 Kellmore Vale, NSW Australia 2563
info@corvanwellandcare.com

(back of card to include website www.corvanwellandcare.com

```html
<!DOCTYPE html>
<html lang="en">
<head>
<meta charset="utf-8">
<title>Corvan Wellandcare – Business Card</title>
<link rel="stylesheet" href="https://fonts.googleapis.com/css2?family=Exo+2:wght@400;600;700&family=Titillium+Web:wght@400;600&display=swap">
<style>
  :root {
    --bg: #e9e9e7;
    --card: #ffffff;
    --blue: #1aa3dd;
    --blue-deep: #1d8ccc;
    --green: #4bb84a;
    --ink: #5a5a5a;
    --shadow: rgba(0,0,0,0.18);
  }
  * { margin: 0; padding: 0; box-sizing: border-box; }
  html, body {
    width: 1200px; height: 900px; overflow: hidden;
    background: var(--bg);
  }
  .canvas {
    width: 1200px; height: 900px;
    display: flex; flex-direction: column;
    align-items: center; justify-content: center; gap: 60px;
  }
  .card {
    position: relative;
    width: 540px; height: 309px;
    background: var(--card);
    box-shadow: 0 6px 18px var(--shadow);
    overflow: hidden;
  }
  .card-shapes { position: absolute; inset: 0; }

  /* Brand name in place of logo */
  .brand {
    display: flex; align-items: center; gap: 8px;
    font-family: "Exo 2", sans-serif;
    font-weight: 700;
    color: var(--blue-deep);
    white-space: nowrap;
  }
  .brand-dot {
    flex: none;
    width: 14px; height: 14px; border-radius: 50%;
    background: var(--green);
  }

  /* Back */
  .card-back .brand {
    position: absolute; left: 0; right: 0; top: 112px;
    justify-content: center; font-size: 22px;
  }
  .web-band {
    position: absolute; left: 0; right: 0; top: 160px; height: 24px;
    background: var(--blue-deep);
    color: #fff;
    font-family: "Titillium Web", sans-serif;
    font-weight: 600; font-size: 15px; letter-spacing: 0.5px;
    display: flex; align-items: center; justify-content: center;
  }

  /* Front */
  .card-front .brand-block {
    position: absolute; left: 34px; top: 134px;
  }
  .card-front .brand { font-size: 16px; gap: 7px; }
  .card-front .brand-dot { width: 12px; height: 12px; }
  .tagline {
    margin-top: 2px; margin-left: 19px;
    font-family: "Titillium Web", sans-serif;
    font-size: 6px; letter-spacing: 0.4px;
    color: var(--ink); text-transform: uppercase;
    white-space: nowrap;
  }
  .person {
    position: absolute; left: 34px; top: 208px;
  }
  .person-name {
    font-family: "Exo 2", sans-serif; font-weight: 700;
    font-size: 24px; color: var(--blue-deep); line-height: 1.05;
  }
  .person-role {
    font-family: "Titillium Web", sans-serif;
    font-size: 13px; color: var(--green);
  }
  .contact {
    position: absolute; left: 318px; top: 112px;
    font-family: "Titillium Web", sans-serif;
    font-size: 10.5px; line-height: 1.25; color: var(--ink);
    white-space: nowrap;
  }
  .contact dt { color: var(--blue); }
  .contact dd { margin-bottom: 1px; }
</style>
</head>
<body>
<main class="canvas">

  <section class="card card-back" aria-label="Back of business card">
    <div class="brand"><span class="brand-dot"></span><span>CORVAN WELLANDCARE</span></div>
    <div class="web-band">www.corvanwellandcare.com</div>
  </section>

  <section class="card card-front" aria-label="Front of business card">
    <svg class="card-shapes" viewBox="0 0 540 309" width="540" height="309" aria-hidden="true">
      <path d="M0 0 H540 V22 C430 26 340 70 230 84 C140 95 60 98 0 104 Z" fill="var(--blue)"/>
      <rect x="0" y="295" width="335" height="14" fill="var(--blue)"/>
      <rect x="335" y="295" width="205" height="14" fill="var(--green)"/>
    </svg>

    <div class="brand-block">
      <div class="brand"><span class="brand-dot"></span><span>CORVAN WELLANDCARE</span></div>
      <p class="tagline">Care and risk guidance for every venue</p>
    </div>

    <div class="person">
      <p class="person-name">Dane Morvello</p>
      <p class="person-role">Director &amp; Principal Consultant</p>
    </div>

    <dl class="contact">
      <dt>Phone:</dt>
      <dd>+61 (0) 468502 174</dd>
      <dt>Post Box:</dt>
      <dd>456 Kellmore Vale, NSW Australia 2563</dd>
      <dt>E-mail:</dt>
      <dd>info@corvanwellandcare.com</dd>
    </dl>
  </section>

</main>
</body>
</html>
```